Company Business Card Design Project - Revamp the image of an old construction company.

We need a business card designed for a new company in Australia.

Type of business is Commercial Roofing & Painting.

Medium will be brushed black metal card that can/will be acid etched to a brushed steel silver, acid die cut and two printed colours of our choice which will be white and pantone orange.

We have hopes that the design will be simple, modern and represent with a quick glance what our company does.

Please read instructions carefully in must have box any questions please ask.

If you are interested in this job please look at other job that we have which is very similar with logo and design

Please have a look at the things that can be done with metals cards on yondle images for inspiration.

Target Market(s)

Business owners, commercial property development Men from 25-70 years of age.

Industry/Entity Type

Construction

Requirements
Must have
• Front of card:

Must use the company logo and name provided as attachment (see below kestrel mark construction_black_background).

the words -Commercial Painting and Roofing- must be on front of card

details needed on front or back depending on your design

Name
position
email
mobile

all details can be on front with a cool design to be etched on the back of card or to keep front simple you can put all detail on back of card, I will leave the lay out to you.

Colours in logo are

Pantone 144 C Orange
Pantone 11-0601 White
Pantone 7539 C Gray
Pantone 426 C Black

However black will be the base of black metal card. Gray will be replaced with the etching in card revealing the silver. Orange and white will be printed on card.

Please have fun!!
Should not have
• Please don't clutter the card
No fonts smaller then 7 points

```html
<!DOCTYPE html>
<html lang="en">
<head>
<meta charset="utf-8">
<title>Kestrel Mark Construction – Business Card</title>
<link rel="stylesheet" href="https://fonts.googleapis.com/css2?family=Arimo:wght@400;700&display=swap">
<style>
  :root {
    --card-black: #0b0b0b;
    --band-dark: #1c1c1c;
    --band-mid: #2e2e2e;
    --steel-gray: #8a8c8a;
    --logo-gray: #b4b4b2;
    --print-orange: #f7901e;
    --print-white: #ffffff;
    --page-bg: #ffffff;
    --card-edge: #c9c9c9;
  }
  * { box-sizing: border-box; margin: 0; padding: 0; }
  html, body {
    width: 1200px;
    height: 343px;
    overflow: hidden;
    background: var(--page-bg);
    font-family: "Arimo", Arial, sans-serif;
  }
  .canvas { position: relative; width: 1200px; height: 343px; }

  .card {
    position: absolute;
    top: 1px;
    width: 586px;
    height: 340px;
    background: var(--card-black);
    border: 1px solid var(--card-edge);
    border-radius: 14px;
    overflow: hidden;
  }
  .card--front { left: 3px; }
  .card--back { left: 612px; }

  .card__trim {
    position: absolute; left: 0; top: 0; width: 100%; height: 8px;
    background: var(--print-orange);
  }
  .card__texture {
    position: absolute; left: 0; top: 8px; width: 100%; height: 95px;
    background: linear-gradient(180deg, var(--band-mid) 0%, var(--band-dark) 55%, #141414 100%);
  }
  .card__rule {
    position: absolute; left: 0; top: 103px; width: 100%; height: 7px;
    background: var(--steel-gray);
  }

  /* Front */
  .brand-mark {
    position: absolute; left: 36px; top: 146px;
    width: 64px; height: 64px;
    background: var(--steel-gray);
  }
  .brand-name {
    position: absolute; left: 140px; top: 170px;
    font-weight: 700; font-size: 34px; letter-spacing: 1px;
    color: var(--logo-gray);
    white-space: nowrap;
  }
  .brand-underline {
    position: absolute; left: 324px; top: 213px;
    width: 116px; height: 2px;
    background: var(--logo-gray);
  }
  .tagline {
    position: absolute; left: 140px; top: 228px;
    font-size: 19px; color: var(--print-white);
    white-space: nowrap;
  }
  .roller-art {
    position: absolute; left: 456px; top: 132px;
    width: 110px; height: 190px;
    border-radius: 6px;
    background: linear-gradient(200deg, #9a9a98 0%, var(--print-orange) 45%, #7a4810 100%);
  }

  /* Back */
  .contact-name {
    position: absolute; left: 337px; top: 153px;
    font-weight: 700; font-size: 16px; color: var(--print-white);
  }
  .contact-role {
    position: absolute; left: 337px; top: 179px;
    font-size: 14px; color: var(--print-white);
  }
  .contact-line {
    position: absolute; left: 302px;
    display: flex; align-items: center; gap: 11px;
    font-size: 16px; color: var(--print-white);
    white-space: nowrap;
  }
  .contact-line--email { top: 252px; }
  .contact-line--phone { top: 279px; }
  .contact-line svg { width: 26px; height: 20px; flex: none; }
</style>
</head>
<body>
<div class="canvas">

  <section class="card card--front">
    <div class="card__trim"></div>
    <div class="card__texture" role="img" aria-label="Etched hexagon mesh pattern band"></div>
    <div class="card__rule"></div>

    <div class="brand-mark"></div>
    <div class="brand-name">KESTREL MARK</div>
    <div class="brand-underline"></div>
    <p class="tagline">Commercial Painting and Roofing</p>

    <div class="roller-art" role="img" aria-label="Illustration of a paint roller laying down an orange brush stroke"></div>
  </section>

  <section class="card card--back">
    <div class="card__trim"></div>
    <div class="card__texture" role="img" aria-label="Etched hexagon mesh pattern band"></div>
    <div class="card__rule"></div>

    <h1 class="contact-name">Aaron Whitfield</h1>
    <p class="contact-role">Director</p>

    <p class="contact-line contact-line--email">
      <svg viewBox="0 0 26 20" aria-hidden="true">
        <rect x="1" y="2" width="24" height="16" fill="none" stroke="#ffffff" stroke-width="1.4"/>
        <path d="M1 2 L13 11 L25 2 M1 18 L10 9 M25 18 L16 9" fill="none" stroke="#ffffff" stroke-width="1.2"/>
      </svg>
      aaronw@kestrelmark.com
    </p>
    <p class="contact-line contact-line--phone">
      <svg viewBox="0 0 26 20" aria-hidden="true">
        <circle cx="10" cy="10" r="9" fill="none" stroke="#ffffff" stroke-width="1.3"/>
        <path d="M7 5 C5 8 6 12 9 15 L11 13.5 L9.5 11.5 C8.5 10 8.5 9 9 8 L10.5 7 L9 4.5 Z" fill="#ffffff"/>
      </svg>
      +61 0400 555 019
    </p>
  </section>

</div>
</body>
</html>
```